Natural and organic skincare brand needs label design!

I need labels designed for my natural and organic skincare brand velmurine. The front of the bottles must contain the logo (image attached) and the following words: Formulated by a Naturopath; Anti-aging therapy; Organic Facial Oil; with CoEnzyme Q10 and Rosehip Seed Oil; 100ml e3.38fl.oz. Colours I would like used include black/white/grey/silver and aqua. I also like the grey woodgrain used on my draft website (check out www.velmurine.com.au). The logo should be silver foil (shiny).The final design should be simple and communicate nature and sophistication. Some designs I like are found in the attachments. I intend to use black or white bottles.

women aged 30-50 interested in natural products

Skin Care Product

Serif
Sans Serif
Decorative
Script
• Any

• Dimensions: 62mm (w) x 75mm (H) (front label only)
• Must contain the logo (image attached). The logo should be silver foil (shiny). and the following words are to be included on the label:
• Formulated by a Naturopath;
• Anti-aging Therapy;
• Organic Facial Oil;
• with CoEnzyme Q10 and Rosehip Seed Oil;
• 100ml e3.38fl.oz.
• Colours I would like used include black/white/grey/silver and aqua (turquoise). But I am also open to suggestion. I also like the grey woodgrain used on my draft website (check out www.velmurine.com.au)

```html
<!DOCTYPE html>
<html lang="en">
<head>
<meta charset="utf-8">
<title>velmurine – Organic Facial Oil front label</title>
<link rel="stylesheet" href="https://fonts.googleapis.com/css2?family=Open+Sans:wght@400;600&display=swap">
<style>
  :root {
    --backdrop: #c6c6c6;
    --aqua: #8fdcd7;
    --aqua-soft: #d3f1ee;
    --wood-light: #eeeeea;
    --wood-mid: #d9d9d5;
    --slate: #5d6172;
    --slate-light: #8d909d;
    --ink: #3a3a3c;
    --white: #ffffff;
  }
  html, body {
    margin: 0;
    width: 1200px;
    height: 1200px;
    overflow: hidden;
    background: var(--backdrop);
    font-family: "Open Sans", sans-serif;
  }
  .label {
    position: absolute;
    left: 234px;
    top: 157px;
    width: 732px;
    height: 885px;
    overflow: hidden;
    background: var(--wood-light);
    box-shadow: 0 10px 24px rgba(0,0,0,0.28);
  }
  .label__pattern {
    position: absolute;
    left: 0; top: 0;
    width: 100%;
    height: 253px;
    background: linear-gradient(135deg, var(--aqua-soft), #e6f7f5 50%, var(--aqua-soft));
  }
  .label__woodgrain {
    position: absolute;
    left: 0; top: 253px;
    width: 100%;
    height: 632px;
    background: linear-gradient(180deg, var(--wood-light), var(--wood-mid) 45%, var(--wood-light) 75%, var(--wood-mid));
  }
  .brand-seal {
    position: absolute;
    left: 176px;
    top: 40px;
    width: 361px;
    height: 361px;
    border: 10px solid var(--white);
    border-radius: 50%;
    background: radial-gradient(circle at 40% 35%, var(--slate-light), var(--slate) 70%);
    display: flex;
    align-items: center;
    justify-content: center;
  }
  .brand-seal__name {
    color: var(--white);
    font-weight: 400;
    font-size: 50px;
    letter-spacing: 4px;
  }
  .claims {
    position: absolute;
    left: 154px;
    top: 490px;
    margin: 0;
    padding: 0;
    list-style: none;
  }
  .claims__item {
    display: flex;
    align-items: center;
    height: 51px;
    color: var(--ink);
    font-weight: 600;
    font-size: 21px;
    letter-spacing: 0.7px;
  }
  .claims__leaf {
    width: 40px;
    height: 40px;
    margin-right: 12px;
    flex: none;
  }
  .volume {
    position: absolute;
    left: 0; width: 100%;
    top: 822px;
    margin: 0;
    line-height: 28px;
    text-align: center;
    color: var(--ink);
    font-weight: 600;
    font-size: 20px;
    letter-spacing: 0.5px;
  }
  .label__rule {
    position: absolute;
    left: 0; width: 100%;
    top: 853px;
    height: 8px;
    background: var(--aqua);
  }
</style>
</head>
<body>
  <main class="label">
    <div class="label__pattern" role="img" aria-label="Aqua lattice pattern on white"></div>
    <div class="label__woodgrain" role="img" aria-label="Pale grey woodgrain texture"></div>

    <div class="brand-seal">
      <span class="brand-seal__name">velmurine</span>
    </div>

    <ul class="claims">
      <li class="claims__item">
        <svg class="claims__leaf" viewBox="0 0 40 40" aria-hidden="true"><path d="M4 36 C6 18 18 6 38 4 C36 22 24 34 4 36 Z" fill="var(--aqua)"/></svg>
        Formulated by Neuropath
      </li>
      <li class="claims__item">
        <svg class="claims__leaf" viewBox="0 0 40 40" aria-hidden="true"><path d="M4 36 C6 18 18 6 38 4 C36 22 24 34 4 36 Z" fill="var(--aqua)"/></svg>
        Anti-aging Therapy
      </li>
      <li class="claims__item">
        <svg class="claims__leaf" viewBox="0 0 40 40" aria-hidden="true"><path d="M4 36 C6 18 18 6 38 4 C36 22 24 34 4 36 Z" fill="var(--aqua)"/></svg>
        Organic Facial Oil
      </li>
      <li class="claims__item">
        <svg class="claims__leaf" viewBox="0 0 40 40" aria-hidden="true"><path d="M4 36 C6 18 18 6 38 4 C36 22 24 34 4 36 Z" fill="var(--aqua)"/></svg>
        with CoEnzyme Q10 and Rosehip Seed Oil
      </li>
    </ul>

    <p class="volume">100ml e3.38fl.oz.</p>
    <div class="label__rule"></div>
  </main>
</body>
</html>
```